Business Card Design Project

I am community manager and social media strategist. I need a double sided business card with company logo and name. Looking for something professional, elegant but also a little bit original.

• - The logo and the colours are the company colours and a required to stay.
- The size should be: 84 x 55 mm (or 3.30 x 2.16)
- The file size should be: 1039 x 697 pixels (300 dpi)
- I'd like rounded corners. :)

Use the following contact information for the card:

Léonie Vardin
Stratégie médias sociaux / community management / édition de sites sociaux
mob. : 0687529103
leonie.vardin@postelune.fr
Fil. : @lvardin
Visio : vardin.leonie

```html
<!DOCTYPE html>
<html lang="fr">
<head>
<meta charset="utf-8">
<title>Cartes de visite NOVELIA – trois propositions</title>
<link rel="stylesheet" href="https://fonts.googleapis.com/css2?family=Open+Sans:wght@300;400;600;700&display=swap">
<style>
  :root {
    --brand-blue: #1a87c4;
    --brand-navy: #1b5f96;
    --shadow-blue: #14689a;
    --slate-band: #4d7fa3;
    --label-blue: #2b8fcb;
    --panel-grey: #e3e3e3;
    --card-border: #dcdcdc;
    --ink: #222222;
    --ink-soft: #333333;
    --white: #ffffff;
  }
  * { box-sizing: border-box; margin: 0; padding: 0; }
  html, body { width: 1200px; height: 900px; overflow: hidden; background: var(--white); }
  body { font-family: "Open Sans", Arial, sans-serif; }

  .board { position: relative; width: 1200px; height: 900px; }

  .design-label {
    position: absolute; left: 138px;
    font-size: 34px; font-weight: 300; color: var(--label-blue);
    line-height: 1; transform: translateY(-50%);
  }
  .design-label--one { top: 220px; }
  .design-label--two { top: 456px; }
  .design-label--three { top: 690px; }

  .card {
    position: absolute; width: 339px; height: 203px;
    border: 1px solid var(--card-border); background: var(--white);
    overflow: hidden;
  }
  .card svg { position: absolute; inset: 0; }
  .card > span, .card > div { position: absolute; }

  .card--front { left: 344px; }
  .card--back { left: 721px; }
  .row-one { top: 122px; }
  .row-two { top: 356px; }
  .row-three { top: 590px; }

  .brand-name { font-weight: 700; color: var(--brand-navy); letter-spacing: 0.5px; line-height: 1; white-space: nowrap; }
  .brand-name--small { font-size: 20px; }
  .brand-name--large { font-size: 32px; left: 0; width: 100%; text-align: center; }

  .holder-name { font-size: 12.5px; font-weight: 700; color: var(--white); line-height: 1; white-space: nowrap; }
  .holder-name--blue { color: var(--brand-blue); }

  .detail-list { font-size: 10.5px; line-height: 15px; color: var(--white); white-space: nowrap; }
  .detail-list--dark { color: var(--ink-soft); }
  .detail-line { font-size: 10.5px; line-height: 1; color: var(--white); white-space: nowrap; }
  .detail-line--blue { color: var(--brand-blue); }
  .detail-line--dark { color: var(--ink); }
</style>
</head>
<body>
<main class="board">

  <p class="design-label design-label--one">Design - 1</p>
  <p class="design-label design-label--two">Design - 2</p>
  <p class="design-label design-label--three">Design - 3</p>

  <!-- Design 1 front -->
  <section class="card card--front row-one">
    <svg width="339" height="203" viewBox="0 0 339 203" aria-hidden="true">
      <rect x="12" y="11" width="315" height="181" fill="var(--brand-blue)"/>
      <path d="M12,11 L327,11 L327,19 C260,51 190,106 130,103 C60,106 22,81 12,39 Z" fill="var(--shadow-blue)"/>
      <path d="M12,11 L327,11 L327,13 C260,45 190,100 130,97 C60,100 22,75 12,33 Z" fill="var(--white)"/>
      <circle cx="96" cy="36" r="19" fill="var(--brand-blue)"/>
    </svg>
    <span class="brand-name brand-name--small" style="left:54px; top:60px;">NOVELIA</span>
    <span class="holder-name" style="left:18px; top:130px;">LÉONIE VARDIN</span>
    <div class="detail-list" style="left:188px; top:98px;">
      Stratégie médias sociaux<br>
      Community management<br>
      édition de sites sociaux<br>
      Fil. : @lvardin<br>
      Visio : vardin.leonie<br>
      Mob. : 0687529103
    </div>
    <span class="detail-line" style="left:18px; top:177px;">leonie.vardin@postelune.fr</span>
  </section>

  <!-- Design 1 back -->
  <section class="card card--back row-one">
    <svg width="339" height="203" viewBox="0 0 339 203" aria-hidden="true">
      <circle cx="174" cy="77" r="30" fill="var(--brand-blue)"/>
    </svg>
    <span class="brand-name brand-name--large" style="top:127px;">NOVELIA</span>
  </section>

  <!-- Design 2 front -->
  <section class="card card--front row-two">
    <svg width="339" height="203" viewBox="0 0 339 203" aria-hidden="true">
      <path d="M150,12 L327,12 L327,192 L168,192 C132,160 117,90 150,12 Z" fill="var(--slate-band)"/>
      <path d="M160,12 L327,12 L327,192 L178,192 C142,160 127,90 160,12 Z" fill="var(--brand-blue)"/>
      <circle cx="66" cy="76" r="20" fill="var(--brand-blue)"/>
    </svg>
    <span class="brand-name brand-name--small" style="left:22px; top:104px;">NOVELIA</span>
    <span class="holder-name" style="left:172px; top:43px;">LÉONIE VARDIN</span>
    <div class="detail-list" style="left:172px; top:62px;">
      Stratégie médias sociaux<br>
      community management<br>
      édition de sites sociaux<br>
      Fil. : @lvardin<br>
      Visio : vardin.leonie
    </div>
    <span class="detail-line detail-line--blue" style="left:18px; top:177px;">leonie.vardin@postelune.fr</span>
    <span class="detail-line" style="left:221px; top:177px;">mob. : 0687529103</span>
  </section>

  <!-- Design 2 back -->
  <section class="card card--back row-two">
    <svg width="339" height="203" viewBox="0 0 339 203" aria-hidden="true">
      <path d="M142,13 L330,13 L330,192 L152,192 C122,150 117,60 142,13 Z" fill="var(--panel-grey)"/>
      <path d="M142,13 C117,60 122,150 152,192" fill="none" stroke="var(--brand-blue)" stroke-width="5"/>
      <circle cx="69" cy="77" r="20" fill="var(--brand-blue)"/>
    </svg>
    <span class="brand-name brand-name--small" style="left:24px; top:106px;">NOVELIA</span>
    <span class="holder-name holder-name--blue" style="left:182px; top:97px;">LÉONIE VARDIN</span>
  </section>

  <!-- Design 3 front -->
  <section class="card card--front row-three">
    <svg width="339" height="203" viewBox="0 0 339 203" aria-hidden="true">
      <path d="M185,12 L327,12 L327,125 C270,110 215,60 185,12 Z" fill="var(--brand-blue)"/>
      <rect x="12" y="153" width="315" height="39" fill="var(--brand-blue)"/>
      <circle cx="66" cy="42" r="20" fill="var(--brand-blue)"/>
    </svg>
    <span class="brand-name brand-name--small" style="left:22px; top:70px;">NOVELIA</span>
    <span class="holder-name" style="left:218px; top:21px;">LÉONIE VARDIN</span>
    <div class="detail-list detail-list--dark" style="left:17px; top:99px;">
      Stratégie médias sociaux<br>
      community management<br>
      édition de sites sociaux
    </div>
    <span class="detail-line" style="left:18px; top:158px;">leonie.vardin@postelune.fr</span>
    <span class="detail-line" style="left:18px; top:175px;">mob. : 0687529103</span>
    <span class="detail-line detail-line--dark" style="left:221px; top:159px;">Fil. : @lvardin</span>
    <span class="detail-line detail-line--dark" style="left:221px; top:175px;">Visio : vardin.leonie</span>
  </section>

  <!-- Design 3 back -->
  <section class="card card--back row-three">
    <svg width="339" height="203" viewBox="0 0 339 203" aria-hidden="true">
      <circle cx="174" cy="77" r="30" fill="var(--brand-blue)"/>
    </svg>
    <span class="brand-name brand-name--large" style="top:127px;">NOVELIA</span>
  </section>

</main>
</body>
</html>
```